Heron Dusk business card design

I make handmade colourful women's beaded jewellery (necklaces and earnings).
I require a business card to be designed to truly reflect my jewellery, that is, it is different and stands out.
I would like the business card to look creative, arty, gentle and feminine and fit in with the look of my website and logo (already developed).
I would like the business card to have strong use of the water reeds that are flowing in the wind (please see the banner image on my website www.herondusk-example.com and attached files).

Target Market(s)

Women who are fashion conscious, hip and funky. My audience like things that are a little different and stand out in a crowd.These women are aged in their 20's-40's.

Industry/Entity Type

Jewelry

Contact Information for Business Card

Please include the following items:
1) my logo: Heron Dusk
2) my name, address and phone number: Marla Dorsten, Marrowvale, Australia, 0400 000 000
3) my web details: www.herondusk-example.com, info@herondusk-example.com, www.social-example.com/herondusk

Font styles to use
Other font styles liked:
• Remachine Script

Requirements
Must have
• My business card must have the following:
• 1) my personal details including all my website contacts (see above).
• 2) Heron Dusk logo
• 3) Reeds flowing in the wind (see my banner image on my website www.herondusk-example.com or see attached files).
Nice to have
• A sunrise in the background (rising over water)
• I would prefer that the colour scheme to fit with the Heron Dusk logo, that is the colours of an early morning sunrise i.e yellows, oranges. The use of black and white is fine.
Should not have
• I do not like a commercial manufactured look with hard edges. I would like a look that is soft and reflects an artistic, creative and independent business.

```html
<!DOCTYPE html>
<html lang="en">
<head>
<meta charset="utf-8">
<title>Heron Dusk – Business Card</title>
<link rel="stylesheet" href="https://fonts.googleapis.com/css2?family=Yellowtail&family=Damion&family=Questrial&display=block">
<style>
  :root {
    --ink: #0a0b0b;
    --text-grey: #7b8789;
    --sun-deep: #c9650a;
    --sun-mid: #eb9a1e;
    --sun-glow: #ffd04a;
    --reed-dark: #3a1e08;
  }
  html, body {
    margin: 0;
    padding: 0;
    width: 1200px;
    height: 703px;
    overflow: hidden;
    background: #ffffff;
  }
  .card {
    position: relative;
    width: 1200px;
    height: 703px;
    overflow: hidden;
  }
  .reed-sunset {
    position: absolute;
    inset: 0;
    background:
      radial-gradient(ellipse 420px 520px at 900px 420px, var(--sun-glow) 0%, rgba(255,208,74,0) 70%),
      linear-gradient(160deg, var(--sun-deep) 0%, var(--sun-mid) 45%, #f3b534 70%, var(--reed-dark) 100%);
  }
  .dark-panel {
    position: absolute;
    inset: 0;
    width: 1200px;
    height: 703px;
  }
  .dark-panel polygon { fill: var(--ink); }
  .identity {
    position: absolute;
    left: 53px;
    top: 96px;
  }
  .owner-name {
    margin: 0;
    font-family: "Yellowtail", "Damion", cursive;
    font-weight: 400;
    font-size: 76px;
    line-height: 1;
    color: var(--text-grey);
  }
  .owner-location {
    margin: 4px 0 0 0;
    font-family: "Questrial", sans-serif;
    font-size: 27px;
    color: var(--text-grey);
    letter-spacing: 0.6px;
  }
  .contact-list {
    position: absolute;
    left: 47px;
    top: 311px;
    margin: 0;
    padding: 0;
    list-style: none;
    font-family: "Questrial", sans-serif;
    font-size: 45px;
    line-height: 77px;
    color: var(--text-grey);
    letter-spacing: 0.5px;
    white-space: nowrap;
  }
</style>
</head>
<body>
  <main class="card">
    <div class="reed-sunset" role="img" aria-label="Silhouetted water reeds swaying against a golden sunrise sky"></div>
    <svg class="dark-panel" viewBox="0 0 1200 703" aria-hidden="true">
      <polygon points="0,0 550,0 1004,703 0,703"/>
    </svg>
    <header class="identity">
      <h1 class="owner-name">Marla Dorsten</h1>
      <p class="owner-location">Marrowvale, Australia</p>
    </header>
    <ul class="contact-list">
      <li>Contact details: 0400 000 000</li>
      <li>info@herondusk-example.com</li>
      <li>www.herondusk-example.com</li>
      <li>www.social-example.com/herondusk</li>
    </ul>
  </main>
</body>
</html>
```